Larkspur Ridge Management - Business Cards

I need business cards. My current logo was designed by a designer at this site and I very much like and am happy with the results. I would like a business card that is trendy, unique, current yet professional. I deal with high net worth clients daily

Target Market(s)

Out of state investors looking to get into the rental market in Ohio

Industry/Entity Type

Property Management, Consulting

Contact Information for Business Card

Name, Title (Chief Financial Officer) office phone number (555) 817-3094 website address larkridgemgmt.example

Font styles to use
Sans Serif

Colors
0054AA
0677BA
7BADD7
CADEEF
E8F1F8
0094D4
00A9DD
6FCCEA
C7EBF8
E9F6FB
00AB8E
00BBA5
67D7C9
C6EFE9
E9F9F6

```html
<!DOCTYPE html>
<html lang="en">
<head>
<meta charset="utf-8">
<title>Larkspur Ridge Management – Business Cards</title>
<link href="https://fonts.googleapis.com/css2?family=Inter:wght@400;700;800&display=swap" rel="stylesheet">
<style>
  :root {
    --backdrop: #3b3431;
    --navy: #172a4d;
    --navy-ink: #14264a;
    --red: #d9323a;
    --white: #ffffff;
    --text: #2b3040;
  }
  * { margin: 0; padding: 0; box-sizing: border-box; }
  html, body { width: 1200px; height: 1200px; overflow: hidden; }
  body {
    background: var(--backdrop);
    font-family: "Inter", sans-serif;
    position: relative;
  }
  .card {
    position: absolute;
    left: 179px;
    width: 861px;
    height: 496px;
    overflow: hidden;
    box-shadow: 0 6px 18px rgba(0,0,0,0.35);
  }
  .card-front { top: 84px; background: var(--navy); }
  .card-back { top: 621px; background: var(--white); }

  .brand-name {
    position: absolute;
    left: 0; right: 0;
    text-align: center;
    color: var(--white);
    font-weight: 800;
    text-transform: uppercase;
    letter-spacing: 0.02em;
    line-height: 1.1;
  }
  .card-front .brand-name { top: 212px; font-size: 40px; }
  .brand-name span { display: block; }

  .back-band {
    position: absolute;
    left: 0; top: 0;
    width: 100%;
    height: 200px;
    background: var(--navy);
  }
  .back-rule {
    position: absolute;
    left: 0; top: 202px;
    width: 100%;
    height: 6px;
    background: var(--red);
  }
  .card-back .brand-name { top: 68px; font-size: 34px; }

  .person {
    position: absolute;
    left: 48px;
    top: 332px;
  }
  .person-name {
    font-size: 31px;
    font-weight: 700;
    color: var(--navy-ink);
    letter-spacing: 0.01em;
    white-space: nowrap;
  }
  .person-title {
    margin-top: 4px;
    font-size: 22px;
    font-weight: 400;
    color: var(--red);
    letter-spacing: 0.12em;
    white-space: nowrap;
  }
  .contact-list {
    position: absolute;
    left: 430px;
    top: 326px;
    list-style: none;
  }
  .contact-item {
    display: flex;
    align-items: center;
    height: 34px;
    font-size: 20px;
    color: var(--text);
    letter-spacing: 0.1em;
    white-space: nowrap;
  }
  .contact-icon {
    width: 22px;
    height: 22px;
    margin-right: 14px;
    flex: none;
  }
</style>
</head>
<body>
  <section class="card card-front">
    <p class="brand-name">Larkspur Ridge<span>Management</span></p>
  </section>

  <section class="card card-back">
    <div class="back-band"></div>
    <div class="back-rule"></div>
    <p class="brand-name">Larkspur Ridge<span>Management</span></p>

    <div class="person">
      <p class="person-name">Name Surename</p>
      <p class="person-title">Chief Financial Officer</p>
    </div>

    <ul class="contact-list">
      <li class="contact-item">
        <svg class="contact-icon" viewBox="0 0 24 24" aria-hidden="true">
          <path fill="#172a4d" d="M6.6 10.8a15 15 0 0 0 6.6 6.6l2.2-2.2a1 1 0 0 1 1-.25 11.4 11.4 0 0 0 3.6.57 1 1 0 0 1 1 1V20a1 1 0 0 1-1 1A17 17 0 0 1 3 4a1 1 0 0 1 1-1h3.5a1 1 0 0 1 1 1c0 1.25.2 2.45.57 3.57a1 1 0 0 1-.25 1z"/>
        </svg>
        (555) 817-3094
      </li>
      <li class="contact-item">
        <svg class="contact-icon" viewBox="0 0 24 24" aria-hidden="true">
          <rect x="2" y="5" width="20" height="14" fill="#172a4d"/>
          <path d="M3 6l9 7 9-7" fill="none" stroke="#fff" stroke-width="1.6"/>
        </svg>
        info@larkridgemgmt.example
      </li>
      <li class="contact-item">
        <svg class="contact-icon" viewBox="0 0 24 24" aria-hidden="true">
          <g fill="none" stroke="#172a4d" stroke-width="1.6">
            <circle cx="12" cy="12" r="9.5"/>
            <ellipse cx="12" cy="12" rx="4.5" ry="9.5"/>
            <path d="M2.5 12h19M4 7h16M4 17h16"/>
          </g>
        </svg>
        www.larkridgemgmt.example
      </li>
    </ul>
  </section>
</body>
</html>
```